Verpackungsdesign-BVS für Haarkosmetik
Trifft genau meinen Vorstellungen. Danke für die professionelle Umsetzung
Zielgruppe
wir verkaufen Haarkosmetik an modebewusste, aktive Friseure. Zielgruppe Sind Kunden im mittleren Alter.
Aufgabenstellung
Ich benötige ein Design für eine Haarpflegeserie. Das Design soll zeitlos aber trotzdem einprägsam erscheinen. Kein verschnörkelter Auftritt. Die Produkte der Haarpflegeserie sollen klar strukturiert, übersichtlich und einprägsam erscheinen. Ich lege ein Bild bei, als Idee. Die Serien sind am Markt platziert und für meine Wünsche nicht nutzbar. Sie sollen nur als Anregung dienen. Meine Flaschen ähneln denen der Marke MIRTO, sind jedoch weiss.
Unser Logo sollte in irgendeiner Form auf dem Produkt ersichtlich sein, jedoch nicht dominant erscheinen. Ich könnte mir vorstellen die drei Anfangsbuchstaben unserer Firma: brauneck-vital-studio, als Buchstabenfolge: bVs auf dem Produkt abgebildet zu sehen.
Bei Fragen bitte ich Sie mich zu Kontakten. Es ist gar nicht so einfach seine Vorstellungen schriftlich zu konkretisieren :-)

```html
<!DOCTYPE html>
<html lang="de">
<head>
<meta charset="utf-8">
<title>bVs Haarpflege – Etiketten</title>
<link rel="stylesheet" href="https://fonts.googleapis.com/css2?family=Titillium+Web:wght@300;400;600;700&display=swap">
<style>
  :root {
    --page-bg: #f4f4f4;
    --label-grey: #b9b9b9;
    --label-white: #ffffff;
    --label-clear: #e8e9eb;
    --brand-red: #dc3439;
    --mark-grey: #8c8c8c;
    --body-grey: #8f8f8f;
    --line-light: rgba(255,255,255,0.6);
    --line-soft: #d9d9d9;
  }
  * { margin: 0; padding: 0; box-sizing: border-box; }
  html, body { width: 826px; height: 1200px; overflow: hidden; }
  body {
    background: var(--page-bg);
    font-family: "Titillium Web", sans-serif;
    position: relative;
  }
  .label {
    position: absolute;
    overflow: hidden;
    box-shadow: 0 2px 10px rgba(0,0,0,0.08);
  }
  .label--shampoo { left: 263px; top: 60px; width: 300px; height: 560px; background: var(--label-grey); }
  .label--spray   { left: 150px; top: 690px; width: 250px; height: 440px; background: var(--label-white); }
  .label--mini    { left: 470px; top: 810px; width: 190px; height: 320px; background: var(--label-clear); }

  .line-name {
    position: absolute;
    writing-mode: vertical-rl;
    transform: rotate(180deg);
    font-weight: 300;
    letter-spacing: 0.04em;
    white-space: nowrap;
    line-height: 1;
  }
  .label--shampoo .line-name { left: 30px; bottom: 70px; font-size: 56px; color: var(--line-light); }
  .label--spray .line-name   { left: 20px; bottom: 70px; font-size: 42px; color: var(--line-soft); }
  .label--mini .line-name    { left: 16px; bottom: 52px; font-size: 32px; color: #c9cacc; }

  .info {
    position: absolute;
    text-align: center;
  }
  .label--shampoo .info { left: 100px; right: 10px; top: 70px; }
  .label--spray .info   { left: 80px; right: 6px; top: 60px; }
  .label--mini .info    { left: 60px; right: 4px; top: 40px; }

  .brand-mark {
    display: inline-flex;
    align-items: center;
    gap: 6px;
    color: var(--mark-grey);
    font-weight: 600;
  }
  .brand-mark::before {
    content: "";
    border: 2px solid var(--mark-grey);
    border-radius: 50%;
  }
  .label--shampoo .brand-mark { font-size: 30px; margin-bottom: 48px; }
  .label--shampoo .brand-mark::before { width: 22px; height: 22px; }
  .label--spray .brand-mark { font-size: 20px; margin-bottom: 26px; }
  .label--spray .brand-mark::before { width: 14px; height: 14px; }
  .label--mini .brand-mark { font-size: 15px; margin-bottom: 18px; gap: 4px; }
  .label--mini .brand-mark::before { width: 10px; height: 10px; border-width: 1.5px; }

  .claim {
    color: var(--brand-red);
    font-weight: 700;
    letter-spacing: 0.08em;
    text-transform: uppercase;
  }
  .label--shampoo .claim { font-size: 15px; line-height: 36px; }
  .label--spray .claim   { font-size: 11px; line-height: 25px; }
  .label--mini .claim    { font-size: 8.5px; line-height: 19px; }

  .benefits { color: var(--body-grey); font-weight: 400; letter-spacing: 0.03em; }
  .label--shampoo .benefits { font-size: 10.5px; line-height: 18px; margin-top: 30px; color: #8a8a8a; }
  .label--spray .benefits   { font-size: 8px; line-height: 13px; margin-top: 22px; color: #b0b0b0; }
  .label--mini .benefits    { font-size: 6.5px; line-height: 10px; margin-top: 16px; color: #b5b5b5; }

  .product-band {
    position: absolute;
    background: var(--brand-red);
    color: #fff;
    text-align: center;
    text-transform: uppercase;
  }
  .label--shampoo .product-band { left: 30px; right: 30px; bottom: 34px; height: 24px; line-height: 24px; font-size: 13px; letter-spacing: 0.22em; }
  .label--spray .product-band   { left: 18px; right: 18px; bottom: 36px; height: 18px; line-height: 18px; font-size: 10px; font-weight: 700; letter-spacing: 0.12em; text-align: right; padding-right: 12px; }
  .label--mini .product-band    { left: 14px; right: 14px; bottom: 26px; height: 13px; line-height: 13px; font-size: 7.5px; font-weight: 700; letter-spacing: 0.1em; text-align: right; padding-right: 8px; }
</style>
</head>
<body>

<section class="label label--shampoo">
  <div class="line-name">TRUE COLOUR</div>
  <div class="info">
    <div class="brand-mark">bVs</div>
    <div class="claim">Für<br>Coloriertes<br>Haar</div>
    <p class="benefits">Farbschutz mit UV-Filter<br>Schützt und pflegt das Haar<br>für eine langanhaltende<br>strahlende Farbe</p>
  </div>
  <div class="product-band">Shampoo</div>
</section>

<section class="label label--spray">
  <div class="line-name">FREE FORM</div>
  <div class="info">
    <div class="brand-mark">bVs</div>
    <div class="claim">Für<br>Coloriertes<br>Haar</div>
    <p class="benefits">Farbschutz mit UV-Filter<br>Schützt und pflegt das Haar<br>für eine langanhaltende<br>strahlende Farbe</p>
  </div>
  <div class="product-band">Spray Normal</div>
</section>

<section class="label label--mini">
  <div class="line-name">FREE FORM</div>
  <div class="info">
    <div class="brand-mark">bVs</div>
    <div class="claim">Für<br>Coloriertes<br>Haar</div>
    <p class="benefits">Farbschutz mit UV-Filter<br>Schützt und pflegt das Haar<br>für eine langanhaltende<br>strahlende Farbe</p>
  </div>
  <div class="product-band">Spray Normal</div>
</section>

</body>
</html>
```